Brisk Bookings needs a New Home page

We provide online appointment scheduling. There are many schedulers out there. Ours is unique because the scheduler is shown in one compact view that can be easily incorporated into the customer's website or Chatterloop page. Whether our customer is a solo hair-stylist or a large testing center with hundreds of testing seats at multiple locations, our customer still gets the same easy-to-use, one-page scheduling experience.

Our current home page, briskbookings.com, feels cluttered and outdated. We want something more modern and minimal.

Here are web pages we like:
plumtrellis.com
fernquay.com
gossamo.io

We are not unhappy with the current logo or color scheme.

Need very clear call(s) to action (i.e. sign up for trial, schedule a demo).
Design needs to look good on devices of varying size.

Here are some ideas:
“Simple Online Scheduling” - Simple, compact design, easy-to-use & powerful, time-saving, chaos-taming, affordable, one page scheduling
“Stay in touch” - Basic email confirmations, reminders or targeted email notifications for follow-ups, no shows and more
“Multiple locations? No problem” - Schedule for multiple locations on one scheduler -
“Resource Pools” - Batting cages, clerks at the BQT, computers in a lab, pilates reformer machines
“Go Social” - Scheduling for Chatterloop and mobile devices
“Visual Reporting” - Reports
“Trusted” - Testimonials, reliable since 2005, etc.
List of industries (with links to industry-specific pages)

Ultimately want to redevelop the full site.

Reason: Please do not submit any new designs. We are now just wrapping up polling and discussing details. Thank you to all designers who have submitted. We feel lucky to get to chose from many great designs.

Target Market(s)

Audience is very broad including solo entrepreneurs (massage therapist, accountants, lawyers), educational institutions (elementary schools, university departments, advisers, testing centers), health care providers and screening services, to government.

Industry/Entity Type

Online

Requirements
Must have
• Call(s) to action, i.e. sign up for trial, schedule a demo.
• Look good on devices of different sizes.

```html
<!DOCTYPE html>
<html lang="en">
<head>
<meta charset="utf-8">
<title>Brisk Bookings – Easy One Page Scheduling</title>
<link rel="stylesheet" href="https://fonts.googleapis.com/css2?family=Quicksand:wght@300;400;500;700&family=Open+Sans:wght@400;600;700&display=swap">
<style>
:root{
  --green:#9cc03a;
  --green-dark:#86a82c;
  --orange:#f05a28;
  --ink:#3a3a3a;
  --muted:#8a8a8a;
  --soft:#eceef1;
  --band:#e6e9ee;
  --white:#ffffff;
}
*{margin:0;padding:0;box-sizing:border-box}
html,body{width:1200px;height:2437px;overflow:hidden;background:var(--white)}
body{font-family:"Open Sans",Arial,sans-serif;color:var(--ink);position:relative}
.abs{position:absolute}
a{color:inherit;text-decoration:none}

/* header */
.site-header{left:0;top:0;width:1200px;height:61px;background:var(--white)}
.brand{left:122px;top:12px;display:flex;align-items:center;gap:8px;font-family:"Quicksand",sans-serif;font-weight:700;font-size:28px;color:var(--green)}
.brand-dot{width:12px;height:12px;border-radius:50%;background:var(--orange);margin-top:-18px}
.main-nav{left:443px;top:0;display:flex;height:61px}
.main-nav a{display:flex;align-items:center;padding:0 16px;font-size:14px;color:#555}
.main-nav a.active{background:var(--green);color:var(--white);padding:0 18px}
.login-btn{left:1009px;top:0;width:71px;height:24px;background:var(--orange);color:var(--white);font-size:13px;text-align:center;line-height:24px}

/* hero */
.hero{left:0;top:61px;width:1200px;height:467px;background:linear-gradient(160deg,#b59c83 0%,#a89684 35%,#9d968a 60%,#b8b3a8 100%)}
.hero-title{left:137px;top:95px;font-family:"Quicksand",sans-serif;font-weight:300;font-size:58px;letter-spacing:3px;color:var(--white)}
.hero-lead{left:140px;top:196px;font-family:"Quicksand",sans-serif;font-size:23px;line-height:30px;color:var(--white)}
.step-num{display:inline-block;width:28px;height:28px;border:2px solid var(--white);border-radius:50%;text-align:center;line-height:24px;font-size:20px}
.steps{left:140px;top:276px;list-style:none;font-family:"Quicksand",sans-serif;font-size:23px;color:var(--white)}
.steps li{display:flex;align-items:center;gap:16px;height:33px}
.cta-trial{left:166px;top:461px;width:266px;height:44px;background:var(--green);color:var(--white);font-family:"Quicksand",sans-serif;font-size:23px;text-align:center;line-height:44px}
.product-shot{left:600px;top:233px;width:425px;height:285px;border-radius:12px 12px 4px 4px;background:linear-gradient(180deg,#2b2b2b 0,#2b2b2b 8px,#f4f4f4 8px,#e9ece4 88%,#cfd2d6 88%,#b9bcc0 100%)}
.slide-arrow{width:28px;height:34px;background:var(--white);display:flex;align-items:center;justify-content:center}

/* sub nav */
.subnav{left:0;top:528px;width:1200px;height:67px;background:var(--white);border-bottom:1px solid #e3e3e3;display:flex;justify-content:center;gap:68px;align-items:center;font-family:"Quicksand",sans-serif;font-size:16px;letter-spacing:1px;color:#777}
.subnav .current{color:var(--orange)}

/* features */
.features{left:0;top:595px;width:1200px;height:1070px;background:linear-gradient(180deg,#ffffff 0%,#f3f4f6 40%,#e9ebef 100%)}
.feature-art{border-radius:8px}
.feature-title{font-family:"Quicksand",sans-serif;font-weight:400;font-size:48px;color:#222;letter-spacing:1px}
.feature-text{font-size:15px;line-height:24px;color:var(--muted);width:600px}
.feature-link{font-family:"Quicksand",sans-serif;font-size:21px;color:var(--green)}
.waiting{left:0;top:1508px;width:1200px;text-align:center;font-family:"Quicksand",sans-serif;font-size:38px;color:#333;letter-spacing:1px}
.cta-demo{left:483px;top:1583px;width:232px;height:36px;background:var(--green);color:var(--white);font-family:"Quicksand",sans-serif;font-weight:700;font-size:18px;text-align:center;line-height:36px}

/* clients */
.clients-title{left:0;top:1700px;width:1200px;text-align:center;font-family:"Quicksand",sans-serif;font-weight:700;font-size:21px;color:var(--orange)}
.clients-title span{color:var(--green)}
.client{top:1780px;height:40px;font-family:"Quicksand",sans-serif;font-weight:700;font-size:19px;color:#444;display:flex;align-items:center}
.testimonials-link{left:816px;top:1864px;font-size:15px;color:var(--orange);text-decoration:underline}

/* industries */
.industries{left:0;top:1908px;width:1200px;height:305px;background:var(--band)}
.industries-title{left:0;top:1928px;width:1200px;text-align:center;font-family:"Quicksand",sans-serif;font-size:38px;color:#333;letter-spacing:1px}
.industry-col{top:2014px;list-style:none;font-size:15px;line-height:20.7px;color:#666}
.industry-col a{text-decoration:underline}
.full-list{left:0;top:2183px;width:1200px;text-align:center;font-size:15px;color:var(--green);text-decoration:underline}

/* footer */
.footer-col{top:2224px;width:290px;font-size:12px;line-height:17px;color:#444}
.footer-col h4{font-size:12px;font-weight:600;color:var(--orange);margin-bottom:12px}
.footer-col p{margin-bottom:10px}
.ticks{list-style:none}
.ticks li{display:flex;gap:6px;margin-bottom:9px}
.legal{top:2412px;font-size:11px;color:#777}
</style>
</head>
<body>

<header class="site-header abs">
  <a class="brand abs" href="#">Brisk Bookings<span class="brand-dot"></span></a>
  <nav class="main-nav abs">
    <a class="active" href="#">Home</a>
    <a href="#">See it work</a>
    <a href="#">Who it's for</a>
    <a href="#">Our Scheduler</a>
    <a href="#">FREE Trial</a>
    <a href="#">Log in</a>
    <a href="#">About Us</a>
  </nav>
  <a class="login-btn abs" href="#">Login</a>
</header>

<section class="hero abs" role="img" aria-label="Soft blurred background with a dotted world map"></section>
<h1 class="hero-title abs">Easy One Page Scheduling</h1>
<p class="hero-lead abs">Schedule your appointments<br>in just <span class="step-num">5</span> steps</p>
<ul class="steps abs">
  <li><svg width="20" height="18" viewBox="0 0 20 18"><path d="M2 9l6 6L18 2" stroke="#fff" stroke-width="4" fill="none"/></svg>Select a date</li>
  <li><svg width="20" height="18" viewBox="0 0 20 18"><path d="M2 9l6 6L18 2" stroke="#fff" stroke-width="4" fill="none"/></svg>Select a service</li>
  <li><svg width="20" height="18" viewBox="0 0 20 18"><path d="M2 9l6 6L18 2" stroke="#fff" stroke-width="4" fill="none"/></svg>Select an opening</li>
  <li><svg width="20" height="18" viewBox="0 0 20 18"><path d="M2 9l6 6L18 2" stroke="#fff" stroke-width="4" fill="none"/></svg>Enter contact information</li>
  <li><svg width="20" height="18" viewBox="0 0 20 18"><path d="M2 9l6 6L18 2" stroke="#fff" stroke-width="4" fill="none"/></svg>Confirm appointment</li>
</ul>
<a class="cta-trial abs" href="#">Try it now for Free!</a>
<div class="product-shot abs" role="img" aria-label="Laptop showing the one page scheduler with calendar, services and contact form"></div>
<div class="slide-arrow abs" style="left:590px;top:364px"><svg width="12" height="18" viewBox="0 0 12 18"><path d="M10 2L3 9l7 7" stroke="#e24a3a" stroke-width="3" fill="none"/></svg></div>
<div class="slide-arrow abs" style="left:998px;top:364px"><svg width="12" height="18" viewBox="0 0 12 18"><path d="M2 2l7 7-7 7" stroke="#e24a3a" stroke-width="3" fill="none"/></svg></div>

<nav class="subnav abs">
  <a class="current" href="#">KEY FEATURES</a>
  <a href="#">WHO USES BRISKBOOKINGS</a>
  <a href="#">INDUSTRIES</a>
</nav>

<section class="features abs">
  <svg class="abs" style="left:560px;top:1052px" width="80" height="30" viewBox="0 0 80 30"></svg>
</section>

<div class="feature-art abs" style="left:152px;top:630px;width:224px;height:192px;background:radial-gradient(circle at 40% 50%,#f2f2f2 0,#bfc3c7 45%,#eef0f2 70%,transparent 71%)" role="img" aria-label="Wall clock beside a desk calendar"></div>
<h2 class="feature-title abs" style="left:422px;top:650px">Simple Online Scheduling</h2>
<p class="feature-text abs" style="left:426px;top:718px">Short sentence describing the simplicity behind the application. Its length should be as long as this text runs, 2-3 lines at most.</p>
<a class="feature-link abs" style="left:792px;top:776px" href="#">See how it works &gt;</a>

<h2 class="feature-title abs" style="left:130px;top:855px">Go Social!</h2>
<p class="feature-text abs" style="left:134px;top:928px">Scheduling for Chatterloop and mobile devices. Short sentence describing this feature behind the application. Its length should be as long as this text runs, 2-3 lines at most.</p>
<a class="feature-link abs" style="left:134px;top:1002px" href="#">Watch it in action &gt;</a>
<div class="feature-art abs" style="left:741px;top:853px;width:284px;height:162px;background:linear-gradient(135deg,#3b5a9a 0%,#3b5a9a 45%,#e9ecef 46%,#c9cdd2 100%);border-radius:24px" role="img" aria-label="Smartphone with a social app card"></div>

<div class="feature-art abs" style="left:132px;top:1076px;width:244px;height:182px;background:linear-gradient(180deg,#1d1d1d 0,#1d1d1d 6%,#eef0f2 6%,#dfe3e7 80%,#1d1d1d 80%,#1d1d1d 84%,#d5d8dc 84%)" role="img" aria-label="Desktop monitor showing an envelope icon"></div>
<h2 class="feature-title abs" style="left:422px;top:1090px">Stay in touch.</h2>
<p class="feature-text abs" style="left:426px;top:1162px">Basic email confirmations, reminders or targeted email notifications for follow-ups. Same as before. 2-3 lines at most in order for design to be coherent.</p>
<a class="feature-link abs" style="left:832px;top:1222px" href="#">Try it today for Free &gt;</a>

<h2 class="feature-title abs" style="left:130px;top:1318px">Multiple Locations?</h2>
<p class="feature-text abs" style="left:134px;top:1390px">No problem! Short sentence describing this feature behind the application. Its length should be as long as this text runs, 2-3 lines at most.</p>
<a class="feature-link abs" style="left:134px;top:1446px" href="#">Find out more &gt;</a>
<div class="feature-art abs" style="left:852px;top:1310px;width:196px;height:192px;border-radius:50%;background:radial-gradient(circle at 40% 35%,#7cc4f0 0,#2f7fc2 55%,#1f5e98 100%)" role="img" aria-label="Globe with location pins"></div>

<p class="waiting abs">What are you waiting for?</p>
<a class="cta-demo abs" href="#">Schedule a demo today</a>

<svg class="abs" style="left:560px;top:1664px" width="80" height="18" viewBox="0 0 80 18"><path d="M0 0h80L40 18z" fill="#e9ebef"/></svg>

<h3 class="clients-title abs">Who uses <span>Brisk Bookings</span></h3>
<span class="client abs" style="left:182px">Harbor Virtual School</span>
<span class="client abs" style="left:400px">Ridgewell University</span>
<span class="client abs" style="left:648px">Lantern Corps</span>
<span class="client abs" style="left:858px;font-size:14px">Brightpath Learning Academy</span>
<a class="testimonials-link abs" href="#">Read all the testimonials &gt;</a>

<section class="industries abs"></section>
<h2 class="industries-title abs">Scheduling online appointments for:</h2>
<svg class="abs" style="left:305px;top:2008px" width="42" height="156" viewBox="0 0 42 156"><path d="M38 3C20 3 22 20 22 40v18c0 12-6 20-18 20 12 0 18 8 18 20v18c0 20-2 37 16 37" stroke="var(--orange)" stroke-width="6" fill="none" stroke-linecap="round"/></svg>
<svg class="abs" style="left:850px;top:2008px" width="42" height="156" viewBox="0 0 42 156"><path d="M4 3c18 0 16 17 16 37v18c0 12 6 20 18 20-12 0-18 8-18 20v18c0 20 2 37-16 37" stroke="var(--orange)" stroke-width="6" fill="none" stroke-linecap="round"/></svg>
<ul class="industry-col abs" style="left:374px">
  <li><a href="#">accounting</a></li><li><a href="#">acupuncture</a></li><li><a href="#">automotive</a></li><li><a href="#">advising</a></li><li><a href="#">barber</a></li><li><a href="#">chiropractic</a></li><li><a href="#">counseling</a></li>
</ul>
<ul class="industry-col abs" style="left:552px">
  <li><a href="#">dental</a></li><li><a href="#">education</a></li><li><a href="#">fitness</a></li><li><a href="#">government</a></li><li><a href="#">hair removal</a></li><li><a href="#">health</a></li><li><a href="#">home services</a></li>
</ul>
<ul class="industry-col abs" style="left:721px">
  <li><a href="#">homeopathy</a></li><li><a href="#">interviewing</a></li><li><a href="#">laser equipment</a></li><li><a href="#">legal</a></li><li><a href="#">martial arts</a></li><li><a href="#">massage</a></li><li><a href="#">medical</a></li>
</ul>
<a class="full-list abs" href="#">See the full list &gt;</a>

<footer>
  <div class="footer-col abs" style="left:122px">
    <h4>Easy to Use.</h4>
    <p>Our appointment scheduler is a rich internet application (RIA). Updates occur quickly on a single compact page making it easy for clients to shop for an ideal opening.</p>
    <p>That is important, especially when your appointment calendar is filling up and availability is limited.</p>
  </div>
  <div class="footer-col abs" style="left:497px">
    <h4>Affordable.</h4>
    <p>Online appointment scheduling starts at just $10/month with the Solo Plan. All plans offer:</p>
    <ul class="ticks">
      <li><svg width="12" height="12" viewBox="0 0 12 12"><path d="M1 6l3 3 7-8" stroke="var(--orange)" stroke-width="2.5" fill="none"/></svg>Unlimited appointments and unlimited users.</li>
      <li><svg width="12" height="12" viewBox="0 0 12 12"><path d="M1 6l3 3 7-8" stroke="var(--orange)" stroke-width="2.5" fill="none"/></svg>No sneaky charges for high appointment scheduling volume or additional logins.</li>
    </ul>
  </div>
  <div class="footer-col abs" style="left:818px">
    <h4>Powerful.</h4>
    <p>The online appointment scheduler scales up to meet your growing business needs. Try our online scheduling demos to see how we can handle:</p>
    <ul class="ticks">
      <li><svg width="12" height="12" viewBox="0 0 12 12"><path d="M1 6l3 3 7-8" stroke="var(--orange)" stroke-width="2.5" fill="none"/></svg>Many schedules.</li>
      <li><svg width="12" height="12" viewBox="0 0 12 12"><path d="M1 6l3 3 7-8" stroke="var(--orange)" stroke-width="2.5" fill="none"/></svg>Complex service menus.</li>
      <li><svg width="12" height="12" viewBox="0 0 12 12"><path d="M1 6l3 3 7-8" stroke="var(--orange)" stroke-width="2.5" fill="none"/></svg>Multiple locations</li>
    </ul>
  </div>
  <svg class="abs" style="left:230px;top:2405px" width="740" height="2" viewBox="0 0 740 2"><path d="M0 1h740" stroke="#ddd"/></svg>
  <span class="abs" style="left:590px;top:2392px;width:14px;height:14px;border-radius:50%;background:var(--orange)"></span>
  <p class="legal abs" style="left:234px">Copyright 2013 Brisk Bookings</p>
  <p class="legal abs" style="left:624px">Copyright | Privacy and Billing Policies | Terms and Conditions</p>
</footer>

</body>
</html>
```